QV - menu design

Hi,

We require elegant menu design for upscale restaurant. Please find attached the logo and the menu items for your reference.

for inspiration, this is a good website: -
http://www.platewhisper.example/bellfoldnotes/about.php

We are very much open for Menu Size suggestions.

unfortunately the place is going under renovation, we don't have updated images to it. the closest look and feel to our place is http://varnelo.example ..

we are also open for creative options on the shape, the styles, etc. as long as it represents the fine dine feel ...

Thanks ...

Dear All,

We wouldlike to extend our apology for not being able to provide feedbacks on everysingle design. We were extremely busy and we have multiple contests opensimultaneously which makes the process even harder.

However,we would like to thank you all for the efforts you have put into designingour menu. It is very much appreciated …

We wishyou all success in your design ventures and we are quite positive that we willbe working with many of you on many projects in the soon future. 

Thanks & Regards,

TLG Team...

 

 

 

Industry/Entity Type

Restaurant

Requirements
Must have
• Please ensure that there are 'some' images in the menu ... this is very important.
Should not have
• IMPORTANT: -

1. Please DO NOT insert any currency sign to the menu
2. Please keep the prices of the menu at the end of the menu items descriptions NOT beside the menu item names. The font of the price should be similar to the menu item description and please DO NOT bold the numbers. the prices should be subtle.

Thank you ...

```html
<!DOCTYPE html>
<html lang="en">
<head>
<meta charset="utf-8">
<title>QV Café – Menu Design</title>
<link href="https://fonts.googleapis.com/css2?family=Italianno&family=PT+Sans+Narrow:wght@400;700&family=Arimo&display=swap" rel="stylesheet">
<style>
:root{
  --stage:#2a231e;
  --frame:#8a6a2e;
  --paper-light:#cfa862;
  --paper-mid:#a57a3a;
  --paper-dark:#5e3f17;
  --tag:#e6cf94;
  --tag-shade:#d2b473;
  --ink:#2b2418;
  --gold:#f5c21a;
  --cream:#fff6e2;
  --label:#ffffff;
}
*{margin:0;padding:0;box-sizing:border-box}
html,body{width:947px;height:1200px;overflow:hidden}
body{background:var(--stage);position:relative;font-family:"PT Sans Narrow",sans-serif;color:var(--cream)}
.panel{position:absolute;border:4px solid var(--frame);overflow:hidden;
  background:radial-gradient(ellipse at 50% 35%,var(--paper-light) 0%,var(--paper-mid) 55%,var(--paper-dark) 100%);
  box-shadow:0 4px 14px rgba(0,0,0,.55)}
.panel--front{left:48px;top:38px;width:394px;height:504px}
.panel--back{left:486px;top:38px;width:392px;height:502px}
.panel--inner-one{left:46px;top:624px;width:394px;height:504px}
.panel--inner-two{left:486px;top:622px;width:391px;height:502px}
.caption{position:absolute;font-family:"Arimo",sans-serif;font-size:18px;color:var(--label);width:200px;text-align:center}
.tag{position:absolute;background:linear-gradient(var(--tag),var(--tag-shade));display:flex;align-items:center;justify-content:center;
  clip-path:polygon(0 0,100% 0,100% 82%,50% 100%,0 82%)}
.brand{font-family:"PT Sans Narrow",sans-serif;font-weight:400;color:var(--ink);letter-spacing:4px;line-height:1}
.photo{position:absolute}
.thumb{position:absolute;border:3px solid #fff;border-radius:10px}
.script{font-family:"Italianno",cursive;color:var(--gold);line-height:1}
.menu-title{position:absolute;left:0;width:100%;top:182px;text-align:center;font-size:96px}
.section-title{position:absolute;font-size:46px;z-index:2}
.item{position:absolute;left:12px;width:370px;z-index:2}
.item-name{font-family:"Italianno",cursive;color:var(--gold);font-size:22px;line-height:1}
.item-desc{font-size:9.5px;line-height:11.5px;width:345px;margin-top:2px}
.price{position:absolute;right:0;bottom:0;font-size:9.5px;line-height:11.5px;color:var(--gold)}
.soup-item .item-name{font-size:19px}
.soup-item .item-desc{width:225px;margin-top:1px}
.address{position:absolute;top:416px;width:100%;text-align:center;font-family:"Arimo",sans-serif;font-size:11px;line-height:15px;color:#fff}
</style>
</head>
<body>

<!-- Front cover -->
<section class="panel panel--front">
  <div class="tag" style="left:58px;top:-4px;width:272px;height:150px"><span class="brand" style="font-size:50px">QV</span></div>
  <div class="script menu-title">Menu</div>
  <div class="photo" role="img" aria-label="Roast chicken with vegetables, glasses of juice and fresh citrus fruit"
       style="left:0;top:300px;width:100%;height:204px;background:linear-gradient(100deg,#8a4b1f 0%,#c0792e 35%,#e9a93a 60%,#d9472f 78%,#e8c43a 100%)"></div>
</section>
<div class="caption" style="left:143px;top:563px">Front</div>

<!-- Back cover -->
<section class="panel panel--back">
  <div class="thumb" role="img" aria-label="Fruit dessert cups" style="left:14px;top:176px;width:113px;height:78px;background:linear-gradient(#d8485a,#f1c86a)"></div>
  <div class="thumb" role="img" aria-label="Grilled panini sandwich" style="left:139px;top:176px;width:113px;height:78px;background:linear-gradient(#6b3a1a,#c98a45)"></div>
  <div class="thumb" role="img" aria-label="Bowl of noodle soup" style="left:264px;top:176px;width:113px;height:78px;background:linear-gradient(#c9b27a,#e9dca8)"></div>
  <div class="brand" style="position:absolute;top:330px;width:100%;text-align:center;font-size:38px">QV</div>
  <p class="address">Address: Lorem ipsum dolor sit amet,<br>consectetur adipisicing elit</p>
</section>
<div class="caption" style="left:582px;top:563px">Back</div>

<!-- Inner 1: Breakfast -->
<section class="panel panel--inner-one">
  <div class="photo" role="img" aria-label="Glass of orange juice with orange slices, faded"
       style="left:0;top:290px;width:100%;height:214px;background:linear-gradient(rgba(233,150,40,0),rgba(220,120,40,.55) 60%,rgba(190,70,30,.75))"></div>
  <div class="tag" style="left:236px;top:-4px;width:146px;height:82px"><span class="brand" style="font-size:30px">QV</span></div>
  <div class="script section-title" style="left:12px;top:18px">The Breakfast</div>
  <div class="thumb" role="img" aria-label="Basket of croissants" style="left:238px;top:126px;width:112px;height:70px;background:linear-gradient(#8a5422,#d89a4a)"></div>

  <div class="item" style="top:88px"><div class="item-name">Butter Croissant</div><p class="item-desc">Served plain with a selection of two jams, a vanilla custard cream, a chocolate Cream and butter curls).</p><span class="price">36</span></div>
  <div class="item" style="top:131px"><div class="item-name">Cheese Croissant</div><p class="item-desc">Crumbly freshly baked with cheese filling.</p><span class="price">29</span></div>
  <div class="item" style="top:174px"><div class="item-name">Daily Fresh Eggs</div><p class="item-desc">A choice of poached, scrambled, pan fried, omelet) all served with toasted Bread, mushrooms, roasted tomatoes and chicken sausages.</p><span class="price">59</span></div>
  <div class="item" style="top:228px"><div class="item-name">Healthy Time</div><p class="item-desc">One choice of hot beverage from our cafe served with fruit salad, natural Yoghurt, whole wheat bread vegetable sandwiches and sugar free biscuits selection.</p><span class="price">49</span></div>
  <div class="item" style="top:281px"><div class="item-name">Energy Time</div><p class="item-desc">One choice of hot beverage from our cafe served with finger chocolate muffins, Poached egg with toasted bread and crispy beef bacon, crepe roll with goat Cheese and honey and finger chocolate cream with salted cookies.</p><span class="price">59</span></div>
  <div class="item" style="top:346px"><div class="item-name">QV Time</div><p class="item-desc">One choice of hot beverage from our cafe served with our selection of scones, Smoked salmon and avocado sandwich, roasted sausages sandwich, grilled vegetables sandwich, selection of our best biscuits.</p><span class="price">59</span></div>
  <div class="item" style="top:400px"><div class="item-name">The Arabic Breakfast</div><p class="item-desc" style="width:260px">Choice of Zattar Manakish and Cheese Manakish, served with one choice of hot beverage from our cafe and fresh orange juice.</p><span class="price">59</span></div>
</section>
<div class="caption" style="left:144px;top:1152px">Inner 1</div>

<!-- Inner 2: Sandwiches & Soup -->
<section class="panel panel--inner-two">
  <div class="tag" style="left:8px;top:-4px;width:146px;height:82px"><span class="brand" style="font-size:30px">QV</span></div>
  <div class="script section-title" style="left:176px;top:18px">The Sandwiches</div>
  <div class="thumb" role="img" aria-label="Club sandwich with tomato and lettuce" style="left:268px;top:126px;width:114px;height:74px;background:linear-gradient(#c98a3e,#d9483a 55%,#6aa93a)"></div>
  <div class="photo" role="img" aria-label="Bowl of vegetable and chickpea soup" style="left:226px;top:348px;width:165px;height:150px;border-radius:28px 0 0 0;background:radial-gradient(circle at 55% 55%,#c9b067 0%,#6f8a2e 45%,#e8e1cf 72%,#5e3f17 100%)"></div>

  <div class="item" style="top:84px"><div class="item-name">Grilled Vegetables Sandwich</div><p class="item-desc" style="margin-top:4px">with fresh Goat cheese and chives served with our Homemade spicy garlic mayo.</p><span class="price">59</span></div>
  <div class="item" style="top:132px"><div class="item-name">Butterfish burger</div><p class="item-desc" style="margin-top:4px;width:250px">with fresh tomato, beef bacon, grilled vegetables and béarnaise sauce.</p></div>
  <div class="item" style="top:178px"><div class="item-name">Tataki Tuna sandwich</div><p class="item-desc" style="margin-top:4px">with red onion slices, stewed endives and black olives and sultanas pate.</p><span class="price">79</span></div>
  <div class="item" style="top:222px"><div class="item-name">Beef sirloin steak sandwich</div><p class="item-desc" style="margin-top:4px">grain mustard, Parmesan cheese and fresh Nashi pears.</p><span class="price">79</span></div>
  <div class="item" style="top:266px"><div class="item-name">The Traditional Club sandwich served</div><p class="item-desc" style="margin-top:4px">with French fries and vegetable chips.</p><span class="price">69</span></div>
  <div class="item" style="top:311px"><div class="item-name">Chicken sandwich</div><p class="item-desc" style="margin-top:4px">with Parmesan cheese slices, sundried tomatoes and mint Flavored mayo.</p><span class="price">69</span></div>

  <div class="script section-title" style="left:146px;top:348px;font-size:42px">Soup</div>
  <div class="item soup-item" style="top:390px;left:8px"><div class="item-name">Bouillabaisse</div><p class="item-desc">Traditional French Seafood soup, with Saffron and Estragon.</p><span class="price">119</span></div>
  <div class="item soup-item" style="top:424px;left:8px"><div class="item-name">Barley soup</div><p class="item-desc">With fresh vegetables, tomato smoothie and a hint of garlic oil.</p><span class="price">49</span></div>
  <div class="item soup-item" style="top:458px;left:8px"><div class="item-name">Beef chili</div><p class="item-desc">Served with Arabic bread, fresh guacamole and spicy black beans.</p><span class="price">49</span></div>
</section>
<div class="caption" style="left:582px;top:1152px">Inner 2</div>

</body>
</html>
```